Corvane Bookkeeping Services business cards

looking for a double sided business card design. My logo is attached. I am looking for a design similar to the attached. Keen to see what my logo in white on the blue background would look like.

```html
<!DOCTYPE html>
<html lang="en">
<head>
<meta charset="utf-8">
<title>Corvane Bookkeeping Services – Business Cards</title>
<link rel="stylesheet" href="https://fonts.googleapis.com/css2?family=Open+Sans:wght@400;700&display=swap">
<style>
  :root {
    --stage: #232323;
    --navy: #1f3a6b;
    --navy-deep: #1b3260;
    --green: #9fba3a;
    --ink: #2b2b2b;
    --paper: #ffffff;
  }
  * { box-sizing: border-box; margin: 0; padding: 0; }
  html, body { width: 1200px; height: 780px; overflow: hidden; }
  body {
    background: var(--stage);
    font-family: "Open Sans", Arial, sans-serif;
    position: relative;
  }
  .card {
    position: absolute;
    width: 550px;
    height: 314px;
    border-radius: 22px;
    overflow: hidden;
  }
  .card--front {
    left: 30px; top: 233px;
    background: var(--navy);
    border-bottom: 5px solid var(--green);
  }
  .card--back {
    left: 620px; top: 233px;
    background: var(--paper);
  }

  .brand {
    display: flex;
    align-items: center;
    gap: 14px;
    font-weight: 700;
    line-height: 1.05;
  }
  .brand__mark { flex: none; }
  .brand__name { display: block; }

  .card--front .brand {
    position: absolute;
    left: 0; right: 0; top: 50%;
    transform: translateY(-50%);
    justify-content: center;
    color: var(--paper);
    font-size: 40px;
  }
  .card--front .brand__mark { width: 50px; height: 50px; background: var(--paper); }

  .card--back .brand {
    position: absolute;
    left: 36px; top: 120px;
    color: var(--navy);
    font-size: 25px;
    width: 250px;
  }
  .card--back .brand__mark { width: 32px; height: 32px; background: var(--green); }

  .divider {
    position: absolute;
    left: 300px; top: 44px;
    width: 1.5px; height: 170px;
    background: var(--green);
  }
  .contact {
    position: absolute;
    left: 322px; top: 40px;
    color: var(--ink);
    font-size: 13px;
    line-height: 1.35;
  }
  .contact__name {
    color: var(--green);
    font-weight: 700;
    font-size: 17px;
    letter-spacing: .3px;
    line-height: 1.1;
  }
  .contact__role { margin-bottom: 9px; }
  .contact__address { margin-bottom: 8px; }
  .contact__list { list-style: none; }
  .contact__list li { display: flex; align-items: center; gap: 7px; }
  .contact__list svg { width: 11px; height: 11px; flex: none; }

  .swoosh { position: absolute; left: 0; bottom: 0; width: 550px; height: 120px; }
</style>
</head>
<body>

  <section class="card card--front" aria-label="Card front">
    <div class="brand">
      <span class="brand__mark" aria-hidden="true"></span>
      <span class="brand__name">Corvane<br>Bookkeeping Services</span>
    </div>
  </section>

  <section class="card card--back" aria-label="Card back">
    <div class="brand">
      <span class="brand__mark" aria-hidden="true"></span>
      <span class="brand__name">Corvane<br>Bookkeeping Services</span>
    </div>

    <div class="divider"></div>

    <div class="contact">
      <p class="contact__name">ELLIOT MARSH</p>
      <p class="contact__role">Managing Director</p>
      <p class="contact__address">Your address, City<br>State, Zip 1234</p>
      <ul class="contact__list">
        <li>
          <svg viewBox="0 0 12 12" aria-hidden="true"><path fill="#9fba3a" d="M2.5 1l2 2.3-1 1.2a7 7 0 0 0 4 4l1.2-1 2.3 2-1.2 1.5C5 11 1 7 1 2.2z"/></svg>
          123 456 789
        </li>
        <li>
          <svg viewBox="0 0 12 12" aria-hidden="true"><rect x="3" y="1" width="6" height="10" rx="1" fill="none" stroke="#9fba3a" stroke-width="1.3"/></svg>
          123 456 789
        </li>
        <li>
          <svg viewBox="0 0 12 12" aria-hidden="true"><rect x="1" y="2.5" width="10" height="7" fill="none" stroke="#9fba3a" stroke-width="1.2"/><path d="M1 2.5l5 4 5-4" fill="none" stroke="#9fba3a" stroke-width="1.2"/></svg>
          info@yourmail.com
        </li>
        <li>
          <svg viewBox="0 0 12 12" aria-hidden="true"><circle cx="6" cy="6" r="5" fill="#9fba3a"/><path d="M1 6h10M6 1c-2.5 3-2.5 7 0 10M6 1c2.5 3 2.5 7 0 10" fill="none" stroke="#fff" stroke-width=".8"/></svg>
          www.yourwebsite.com
        </li>
      </ul>
    </div>

    <svg class="swoosh" viewBox="0 0 550 120" preserveAspectRatio="none" aria-hidden="true">
      <path d="M0 120 L0 95 C120 60 300 80 550 5 L550 120 Z" fill="var(--green)"/>
      <path d="M0 92 C90 55 150 50 190 48 C120 55 60 75 0 100 Z" fill="var(--navy-deep)"/>
      <path d="M400 60 C460 45 510 25 550 0 L550 6 C510 30 460 50 400 60 Z" fill="var(--navy-deep)"/>
    </svg>
  </section>

</body>
</html>
```